Tollbrook needs a modernized design

We would like a modern update (that can be responsive) to our existing website. Attached are the two existing pages we would like new concepts of - our home page and a page about one of our locations.

Tollbrook is provides executive offices and virtual office services. Startups, law firms, and financial services are our primary clients. We would like a professional, clean design, leaning towards minimalist. We intend to greatly reduce/eliminate the long paragraphs of text.

Industry/Entity Type

Business Service

Number of Pages Required

2 page

Requirements
Must have
• A design that can be responsive
Nice to have
• Large image(s) on home page that rotate.

```html
<!DOCTYPE html>
<html lang="en">
<head>
<meta charset="utf-8">
<title>Tollbrook Business Centers</title>
<link href="https://fonts.googleapis.com/css2?family=Montserrat:wght@400;500;600&display=swap" rel="stylesheet">
<style>
:root{
  --navy:#1f3a7a;
  --footer:#2b3f73;
  --red:#d0121b;
  --ink:#333;
  --muted:#555;
  --band:#efefef;
  --blue:#1f3c8c;
  --orange:#f7941d;
  --coral:#e0492f;
  --green:#4cb135;
  --purple:#5c0f9e;
}
*{box-sizing:border-box;margin:0;padding:0}
html,body{width:743px;height:1200px;overflow:hidden;background:#fff}
body{font-family:"Montserrat",sans-serif;color:var(--ink);position:relative}
.header{position:absolute;top:0;left:0;width:743px;height:51px;background:#fff;z-index:3}
.brand{position:absolute;left:46px;top:9px;display:flex;align-items:center;gap:6px}
.brand-dot{width:33px;height:33px;border-radius:50%;background:var(--navy)}
.brand-name{font-size:16px;font-weight:600;color:var(--navy);letter-spacing:.5px}
.nav span{position:absolute;top:21px;font-size:7.6px;font-weight:500;color:#222;text-transform:uppercase;white-space:nowrap}
.cta{position:absolute;left:580px;top:14px;width:117px;height:23px;background:var(--red);color:#fff;font-size:7.8px;font-weight:500;display:flex;align-items:center;justify-content:center;white-space:nowrap}
.hero{position:absolute;top:51px;left:0;width:743px;height:494px;background:linear-gradient(180deg,#e6e2da 0%,#c9c1b3 35%,#6c6a66 65%,#4b4b4c 100%)}
.hero-band{position:absolute;top:167px;left:0;width:743px;height:77px;background:rgba(235,235,235,.85);text-align:center}
.hero-title{margin-top:16px;font-size:23.5px;font-weight:600;color:var(--navy);letter-spacing:-.3px}
.hero-sub{font-size:14px;font-weight:400;color:#222;margin-top:1px}
.arrow{position:absolute;top:191px;width:30px;height:30px;border-radius:50%;background:rgba(255,255,255,.9);display:flex;align-items:center;justify-content:center}
.tiles{position:absolute;top:393px;left:49px;display:flex;gap:10px}
.tile{position:relative;width:122px;height:57px;color:#fff;font-size:9.3px;font-weight:600;text-align:center;display:flex;align-items:center;justify-content:center;line-height:1.15;text-transform:uppercase;padding-bottom:6px}
.tile-toggle{position:absolute;bottom:-7px;left:54px;width:14px;height:14px;border-radius:50%;background:#fff;display:flex;align-items:center;justify-content:center}
.intro{position:absolute;top:545px;left:0;width:743px;height:73px;background:var(--band);text-align:center;font-size:10.2px;font-weight:500;line-height:15px;padding-top:21px;color:#222}
.intro-notch{position:absolute;top:618px;left:361px}
.features{position:absolute;top:648px;left:46px;display:flex;gap:45px}
.feature{width:178px}
.feature-head{display:flex;align-items:center;gap:9px;height:45px}
.feature-icon{width:45px;height:45px;border-radius:50%;border:2px solid var(--navy);display:flex;align-items:center;justify-content:center;background:linear-gradient(90deg,var(--navy) 50%,#fff 50%)}
.feature-title{font-size:14px;font-weight:600;color:var(--navy);line-height:14.5px;text-transform:uppercase}
.feature-text{margin-top:20px;font-size:8.2px;line-height:16px;color:var(--muted);height:118px}
.learn{display:inline-block;border:1px solid var(--navy);color:var(--navy);font-size:6.8px;font-weight:500;padding:5px 6px;text-transform:uppercase}
.special{position:absolute;top:861px;left:0;width:743px;height:131px;background:linear-gradient(180deg,#3a4e6e 0%,#28456d 50%,#6b6a55 100%);text-align:center;color:#fff}
.special-title{margin-top:55px;font-size:12.5px;font-weight:500;text-transform:uppercase}
.special-sub{font-size:9px;font-weight:500;margin-top:4px;text-transform:uppercase}
.footer{position:absolute;top:992px;left:0;width:743px;height:160px;background:var(--footer);color:#fff}
.fcol{position:absolute;top:27px}
.fhead{font-size:9px;font-weight:600;margin-bottom:8px}
.ftext{font-size:7.6px;line-height:11px;color:#d9def0}
.ftext p{margin-bottom:7px}
.badge{position:absolute;left:355px;top:29px;width:121px;height:107px;background:#fff;display:flex;align-items:center;justify-content:center}
.badge-shape{width:80px;height:80px;border-radius:50%;background:#cfd6e6;border:4px solid var(--navy)}
.field{width:131px;height:21px;border-radius:11px;background:#fff;font-size:7.2px;color:#888;padding:6px 12px;margin-bottom:6px}
.subscribe{width:70px;height:21px;border-radius:11px;background:#5466a0;font-size:7.4px;font-weight:600;display:flex;align-items:center;justify-content:center}
.bottom{position:absolute;top:1152px;left:0;width:743px;height:48px;background:#fff}
.legal{position:absolute;left:46px;top:11px;font-size:7.2px;color:#555;line-height:13px}
.social{position:absolute;right:46px;top:14px;display:flex;gap:4px}
.social span{width:20px;height:20px;border-radius:50%;border:1px solid #aaa}
</style>
</head>
<body>
<header class="header">
  <div class="brand"><span class="brand-dot"></span><span class="brand-name">Tollbrook</span></div>
  <nav class="nav"><span style="left:198px">Home</span><span style="left:242px">Properties</span><span style="left:309px">Virtual Tours &amp; Videos</span><span style="left:431px">Photos</span><span style="left:484px">Broker Referrals</span></nav>
  <div class="cta">REQUEST INFORMATION</div>
</header>

<section class="hero" role="img" aria-label="Business team meeting around a table in a bright glass-walled office">
  <div class="hero-band">
    <div class="hero-title">ON DEMAND MEETING ROOMS</div>
    <div class="hero-sub">THAT FIT YOUR NEEDS AND YOUR BUDGET</div>
  </div>
  <div class="arrow" style="left:45px"><svg width="10" height="12" viewBox="0 0 10 12"><path d="M7 1 2 6l5 5" fill="none" stroke="#333" stroke-width="2"/></svg></div>
  <div class="arrow" style="left:667px"><svg width="10" height="12" viewBox="0 0 10 12"><path d="M3 1l5 5-5 5" fill="none" stroke="#333" stroke-width="2"/></svg></div>
  <div class="tiles">
    <div class="tile" style="background:var(--blue)">Executive Office<br>Suites<span class="tile-toggle"><svg width="8" height="5"><path d="M1 1l3 3 3-3" fill="none" stroke="#1f3c8c" stroke-width="1.3"/></svg></span></div>
    <div class="tile" style="background:var(--orange)">On-Demand<br>Meeting Rooms<span class="tile-toggle"><svg width="8" height="5"><path d="M1 1l3 3 3-3" fill="none" stroke="#f7941d" stroke-width="1.3"/></svg></span></div>
    <div class="tile" style="background:var(--coral)">On-Demand<br>Training Rooms<span class="tile-toggle"><svg width="8" height="5"><path d="M1 1l3 3 3-3" fill="none" stroke="#e0492f" stroke-width="1.3"/></svg></span></div>
    <div class="tile" style="background:var(--green)">Virtual Office<br>Solutions<span class="tile-toggle"><svg width="8" height="5"><path d="M1 1l3 3 3-3" fill="none" stroke="#4cb135" stroke-width="1.3"/></svg></span></div>
    <div class="tile" style="background:var(--purple)">Video Conference<br>Solutions<span class="tile-toggle"><svg width="8" height="5"><path d="M1 1l3 3 3-3" fill="none" stroke="#5c0f9e" stroke-width="1.3"/></svg></span></div>
  </div>
</section>

<section class="intro">Come See Why Smarter Companies are Choosing Tollbrook Business Centers' Dallas, Ft. Worth and<br>Houston Executive Office Suites, Virtual Offices, Meeting Rooms and Video Conferencing.</section>
<svg class="intro-notch" width="20" height="10" viewBox="0 0 20 10"><path d="M0 0h20L10 9z" fill="#efefef"/></svg>

<section class="features">
  <article class="feature">
    <div class="feature-head"><div class="feature-icon"></div><div class="feature-title">Our<br>Value</div></div>
    <p class="feature-text">Either you need Dallas/Ft. Worth Office Space, Dallas Executive Suites, Ft. Worth Executive Suites, Houston Office Space, Houston Executive Suites, or maybe you simply need a place to stop in and use an on-demand office or meeting room from time to time...</p>
    <span class="learn">Learn More</span>
  </article>
  <article class="feature">
    <div class="feature-head"><div class="feature-icon"></div><div class="feature-title">Our<br>Community</div></div>
    <p class="feature-text">Companies that partner with Tollbrook share more than a prestigious address. They also share ideas and services. Our Executive Office Business Centers are places where savvy, growing companies can network, interact and learn from one another...</p>
    <span class="learn">Learn More</span>
  </article>
  <article class="feature">
    <div class="feature-head"><div class="feature-icon"></div><div class="feature-title">Our<br>Service</div></div>
    <p class="feature-text">Tollbrook Business Centers positions its management team in every one of its business centers - we operate with an open-door policy as a medium-sized company without all of the corporate bureaucracy and red tape.</p>
    <span class="learn">Learn More</span>
  </article>
</section>

<section class="special" role="img" aria-label="City skyline of glass office towers at dusk">
  <div class="special-title">View Current Special</div>
  <div class="special-sub">Spring into the perfect office with Tollbrook!</div>
</section>

<footer class="footer">
  <div class="fcol" style="left:46px">
    <div class="fhead">Contact Info</div>
    <div class="ftext">
      <p>228, Lorem Ipsum dolor sit,<br>dosis amet 858485</p>
      <p>Dallas 214.555.0142<br>Houston 713.555.0178</p>
      <p>Website:<br>www.tollbrookoffices.com/</p>
    </div>
  </div>
  <div class="fcol" style="left:212px">
    <div class="fhead">Quick Links</div>
    <div class="ftext" style="line-height:13.6px">Home<br>Properties<br>Virtual Tours &amp; Videos<br>Photos<br>Broker Referrals</div>
  </div>
  <div class="badge"><div class="badge-shape"></div></div>
  <div class="fcol" style="left:547px">
    <div class="fhead">Subscribe Newsletter!</div>
    <div class="field">Name</div>
    <div class="field">Email Address</div>
    <div class="subscribe">SUBSCRIBE</div>
  </div>
</footer>

<div class="bottom">
  <div class="legal">About Us | Contact Us | Forums | Testimonials | Careers | FAQs | Furniture | Specials | Terms of Use | Privacy Policy | Sitemap<br>Copyright © 2016 Tollbrook Business Centers. All Rights Reserved</div>
  <div class="social" aria-label="Social links"><span></span><span></span><span></span><span></span><span></span></div>
</div>
</body>
</html>
```